Pull-up Banner Design Project

We are a managed account investment company specialising in financial derivatives. Sydney based, our team combines over 100 years of financial markets experience. Our advisers trade the worlds financial markets directly on the clients account whilst the client retains full access and control of the account.
We are holding a seminar in September (and potentially more next year) to showcase our specialist investment program and need to create TWO pull-up banners for the event. The banners need to compliment each other as a Right side, Left side of the stage or presenter, however they should be able to be deployed independently. The size of the banners will be approx 120 cm wide by 200 cm tall.
We have an approved company colour pallet, logos and images. I have provided JPEG versions of these however they can be supplied in Bitmap or GIF if required.
Target Market(s)
Self Managed Superannuation Fund Trustees (Individual Investors)
Industry/Entity Type
Investment
Requirements
Must have
- - Two banner designs - One Right of Stage and one Left of Stage
- Company approved logo
- Company approved colour pallet
- Company approved images
- Can be used independently
- Website: www.korvenpartners.com.au (can be smallish print)
- Phone: 1300 416 748 (can be smallish print)
Should not have
- Absolutely no images of obscene wealth such as palm trees or speed boats or similar... approved images only.

```html
<!DOCTYPE html>
<html lang="en">
<head>
<meta charset="utf-8">
<title>Korven Partners – Stage Banners</title>
<link rel="stylesheet" href="https://fonts.googleapis.com/css2?family=Open+Sans:wght@400;700&display=swap">
<style>
  :root {
    --charcoal: #333333;
    --jade: #009173;
    --brand-green: #1e6b3a;
    --white: #ffffff;
    --page: #ffffff;
    --edge: #b5b5b5;
    --stone-light: #4f514c;
    --stone-dark: #262724;
    --sky-blue: #6d8cc0;
    --sky-pale: #b9c6dc;
    --tower-grey: #3a3e45;
  }
  * { box-sizing: border-box; margin: 0; padding: 0; }
  html, body {
    width: 1200px; height: 971px; overflow: hidden;
    background: var(--page);
    font-family: "Open Sans", Arial, sans-serif;
  }
  .stage { position: relative; width: 1200px; height: 971px; }
  .banner {
    position: absolute; top: 18px; width: 569px; height: 946px;
    border: 1px solid var(--edge);
    display: flex; flex-direction: column;
    --frame-x: 71px; --headline-x: 98px;
  }
  .banner--left { left: 15px; --tone: var(--charcoal); }
  .banner--right { left: 631px; --tone: var(--jade); --frame-x: 65px; --headline-x: 94px; }

  .banner__headline-panel {
    position: relative; height: 423px; background: var(--tone);
  }
  .banner__frame { position: absolute; left: var(--frame-x); top: 71px; }
  .banner__headline {
    position: absolute; left: var(--headline-x); top: 106px;
    color: var(--white); font-weight: 700;
    font-size: 44.5px; line-height: 51.5px; letter-spacing: -0.3px;
    text-transform: uppercase;
  }
  .banner__photo { height: 286px; }
  .banner--left .banner__photo {
    background: radial-gradient(circle at 40% 40%, var(--stone-light) 0%, var(--stone-dark) 100%);
  }
  .banner--right .banner__photo {
    background: linear-gradient(to bottom, var(--sky-blue) 0%, var(--sky-pale) 35%, var(--tower-grey) 100%);
  }
  .banner__brand {
    height: 138px; background: var(--white);
    display: flex; align-items: center; justify-content: center;
  }
  .banner__brand-name {
    color: var(--brand-green); font-weight: 700;
    font-size: 40px; letter-spacing: 1px; text-transform: uppercase;
  }
  .banner__contact {
    flex: 1; background: var(--tone); color: var(--white);
    display: flex; align-items: center; justify-content: center;
    font-size: 20px; gap: 14px;
  }
  .banner__divider { opacity: 0.6; }
</style>
</head>
<body>
<main class="stage">
  <section class="banner banner--left" aria-label="Left of stage banner">
    <div class="banner__headline-panel">
      <svg class="banner__frame" width="434" height="284" viewBox="0 0 434 284" aria-hidden="true">
        <g fill="none" stroke="#fff" stroke-width="3">
          <path d="M1.5 41V1.5H41"/><path d="M393 1.5H432.5V41"/>
          <path d="M1.5 243V282.5H41"/><path d="M393 282.5H432.5V243"/>
        </g>
      </svg>
      <h2 class="banner__headline">Leading<br>Collaborative<br>Comtemporary<br>Professional</h2>
    </div>
    <div class="banner__photo" role="img" aria-label="Photograph of dark polished river pebbles"></div>
    <div class="banner__brand"><span class="banner__brand-name">Korven Partners</span></div>
    <div class="banner__contact"><span>1300 416 748</span><span class="banner__divider">|</span><span>www.korvenpartners.com.au</span></div>
  </section>

  <section class="banner banner--right" aria-label="Right of stage banner">
    <div class="banner__headline-panel">
      <svg class="banner__frame" width="434" height="284" viewBox="0 0 434 284" aria-hidden="true">
        <g fill="none" stroke="#fff" stroke-width="3">
          <path d="M1.5 41V1.5H41"/><path d="M393 1.5H432.5V41"/>
          <path d="M1.5 243V282.5H41"/><path d="M393 282.5H432.5V243"/>
        </g>
      </svg>
      <h2 class="banner__headline">Leading<br>Collaborative<br>Comtemporary<br>Professional</h2>
    </div>
    <div class="banner__photo" role="img" aria-label="Photograph of glass office towers against a cloudy blue sky"></div>
    <div class="banner__brand"><span class="banner__brand-name">Korven Partners</span></div>
    <div class="banner__contact"><span>1300 416 748</span><span class="banner__divider">|</span><span>www.korvenpartners.com.au</span></div>
  </section>
</main>
</body>
</html>
```